TernQuay Business Cards

Create business cards for our exciting new software company. We provide cloud billing systems and provisioning software for campany that need monthly SaaS and Cloud Billing

Target Market(s)

Enterprise businesses, b2b, telecom carriers, software manufactures

Industry/Entity Type

Software

```html
<!DOCTYPE html>
<html lang="en">
<head>
<meta charset="utf-8">
<title>TernQuay Business Cards</title>
<link rel="stylesheet" href="https://fonts.googleapis.com/css2?family=Open+Sans:wght@400;600;700&display=swap">
<style>
  :root {
    --backdrop: #3d6787;
    --card-dark: #2f2f30;
    --card-light: #f1f1f1;
    --ink-dark: #333335;
    --ink-grey: #5c5c5c;
    --logo-grey: #c9c5c5;
    --tagline-grey: #8b8b8b;
    --brand-blue: #1f6fa6;
    --white: #ffffff;
  }
  * { box-sizing: border-box; margin: 0; padding: 0; }
  html, body {
    width: 1200px;
    height: 900px;
    overflow: hidden;
  }
  body {
    position: relative;
    background: var(--backdrop);
    font-family: "Open Sans", Arial, sans-serif;
  }

  .card {
    position: absolute;
    width: 705px;
    height: 420px;
    box-shadow: 0 6px 18px rgba(0, 0, 0, 0.35);
  }

  /* Front: dark card */
  .card-front {
    left: 50px;
    top: 40px;
    background: var(--card-dark);
  }
  .front-brand {
    position: absolute;
    left: 160px;
    top: 205px;
    width: 412px;
    text-align: right;
  }
  .front-brand .brand-name {
    font-size: 64px;
    font-weight: 400;
    color: var(--logo-grey);
    line-height: 1;
    letter-spacing: 1px;
  }
  .front-brand .tagline {
    margin-top: 14px;
    font-size: 12px;
    line-height: 18px;
    letter-spacing: 2.4px;
    color: var(--tagline-grey);
    text-transform: uppercase;
  }

  /* Back: light card */
  .card-back {
    left: 420px;
    top: 390px;
    background: var(--card-light);
  }
  .brand-row {
    position: absolute;
    left: 30px;
    top: 78px;
    display: flex;
    align-items: center;
  }
  .brand-dot {
    width: 56px;
    height: 56px;
    border-radius: 50%;
    background: var(--brand-blue);
    margin: 0 36px 0 28px;
  }
  .brand-divider {
    width: 1px;
    height: 70px;
    background: var(--ink-grey);
    margin-right: 16px;
  }
  .brand-lockup { text-align: right; }
  .brand-lockup .brand-name {
    font-size: 42px;
    font-weight: 700;
    color: var(--brand-blue);
    line-height: 1;
    letter-spacing: 0.5px;
  }
  .brand-lockup .tagline {
    margin-top: 6px;
    font-size: 10px;
    line-height: 14px;
    letter-spacing: 1.6px;
    color: var(--ink-grey);
    text-transform: uppercase;
  }

  .person {
    position: absolute;
    right: 52px;
    top: 192px;
    text-align: right;
  }
  .person-name {
    display: block;
    width: 170px;
    height: 28px;
    background: var(--ink-dark);
    color: var(--white);
    font-size: 19px;
    font-weight: 600;
    line-height: 28px;
    text-align: center;
  }
  .person-role {
    display: inline-block;
    width: 95px;
    height: 24px;
    margin-top: 3px;
    background: var(--brand-blue);
    color: var(--white);
    font-size: 14px;
    line-height: 24px;
    text-align: center;
  }

  .contact-band {
    position: absolute;
    left: 62px;
    top: 302px;
    width: 590px;
    height: 76px;
    background: var(--ink-dark);
    color: var(--white);
    font-size: 14px;
  }
  .contact-item {
    position: absolute;
    display: flex;
    align-items: center;
    gap: 8px;
  }
  .contact-item svg { width: 13px; height: 13px; fill: var(--white); }
  .contact-address { left: 22px; top: 14px; }
  .contact-phone { left: 22px; top: 42px; }
  .contact-email { left: 192px; top: 42px; }
  .contact-web { left: 408px; top: 46px; }
</style>
</head>
<body>

  <section class="card card-front">
    <div class="front-brand">
      <div class="brand-name">TernQuay</div>
      <p class="tagline">Cloud billing and<br>operational support systems</p>
    </div>
  </section>

  <section class="card card-back">
    <div class="brand-row">
      <div class="brand-dot"></div>
      <div class="brand-divider"></div>
      <div class="brand-lockup">
        <div class="brand-name">TERNQUAY</div>
        <p class="tagline">Cloud billing and<br>operational support systems</p>
      </div>
    </div>

    <div class="person">
      <span class="person-name">Name</span>
      <span class="person-role">range</span>
    </div>

    <div class="contact-band">
      <div class="contact-item contact-address">
        <svg viewBox="0 0 16 16" aria-hidden="true"><path d="M8 1 1 7.5h2V15h4v-4h2v4h4V7.5h2z"/></svg>
        <span>Oregon-USA Headquarter</span>
      </div>
      <div class="contact-item contact-phone">
        <svg viewBox="0 0 16 16" aria-hidden="true"><path d="M3.5 1 6 4 4.6 5.6c.9 2.2 3.6 4.9 5.8 5.8L12 10l3 2.5-1.5 2.5C7.5 15 1 8.5 1 2.5z"/></svg>
        <span>000000482</span>
      </div>
      <div class="contact-item contact-email">
        <svg viewBox="0 0 16 16" aria-hidden="true"><path d="M1 6 8 1l7 5v9H1zm1.5 1.2v6.3h11V7.2L8 11z"/></svg>
        <span>info@ternquay.com</span>
      </div>
      <div class="contact-item contact-web">
        <svg viewBox="0 0 16 16" aria-hidden="true"><path d="M8 1a7 7 0 1 0 0 14A7 7 0 0 0 8 1zm0 1.5c.8 0 1.8 1.6 2.1 4.5H5.9C6.2 4.1 7.2 2.5 8 2.5zM4.4 7H2.6a5.5 5.5 0 0 1 3-4C5 4.1 4.6 5.5 4.4 7zm0 2c.2 1.5.6 2.9 1.2 4a5.5 5.5 0 0 1-3-4zm1.5 0h4.2c-.3 2.9-1.3 4.5-2.1 4.5S6.2 11.9 5.9 9zm5.7 0h1.8a5.5 5.5 0 0 1-3 4c.6-1.1 1-2.5 1.2-4zm0-2c-.2-1.5-.6-2.9-1.2-4a5.5 5.5 0 0 1 3 4z"/></svg>
        <span>www.ternquay.com</span>
      </div>
    </div>
  </section>

</body>
</html>
```